Design eines Praxisschilds für Hausarztpraxis
Zielgruppe
Hausarztpraxis, Zielgruppe sind die Bewohner vor Ort, bodenständig
Aufgabenstellung
Praxisschild entwerfen, es soll schlicht sein. Das angefügte Logo bitte verwenden, ggf. auch nur das Symbol ohne Namen verwenden und den Namen extra in schwarz aufführen.
Farben:
- schwarz
- Pantone 13-0645 Limeade
- Pantone 7726
Text:
Dr. med. Jonas Walbrecht
Facharzt für Innere Medizin
Facharzt für Allgemeinmedizin
Sprechzeiten:
Montag bis Freitag 07:30 – 12:00 Uhr
Dienstag und Donnerstag 17:00 – 19:00 Uhr
und nach Vereinbarung
Tel: 0761 83172
www.hausarzt-beispielau.de
Format quer (die Maße sind leider vorgegeben): 55,7 cm x 42,8 cm

```html
<!DOCTYPE html>
<html lang="de">
<head>
<meta charset="utf-8">
<title>Praxisschild – Dr. med. Jonas Walbrecht</title>
<link rel="stylesheet" href="https://fonts.googleapis.com/css2?family=Hanken+Grotesk:wght@400;600;700&display=swap">
<style>
  :root {
    --paper: #ffffff;
    --green: #2a7a4f;
    --lime: #d3d65c;
    --grey: #b9b9b9;
  }
  html, body {
    margin: 0;
    padding: 0;
    overflow: hidden;
    background: var(--paper);
  }
  .sign {
    position: relative;
    width: 1200px;
    height: 922px;
    background: var(--paper);
    font-family: "Hanken Grotesk", sans-serif;
    overflow: hidden;
  }
  .sign__mark {
    position: absolute;
    left: 539px;
    top: 107px;
    width: 106px;
    height: 106px;
  }
  .line {
    position: absolute;
    left: 0;
    width: 100%;
    margin: 0;
    text-align: center;
    line-height: 1;
    white-space: nowrap;
  }
  .doctor-name {
    top: 238px;
    font-size: 43px;
    font-weight: 400;
    letter-spacing: 0.09em;
    color: var(--lime);
    text-transform: uppercase;
  }
  .specialty {
    font-size: 43px;
    font-weight: 400;
    letter-spacing: 0.09em;
    color: var(--green);
    text-transform: uppercase;
  }
  .specialty--internal { top: 297px; }
  .specialty--general { top: 356px; }
  .hours-title {
    top: 419px;
    font-size: 27px;
    font-weight: 700;
    letter-spacing: 0.5em;
    color: var(--lime);
    text-transform: uppercase;
    padding-left: 0.5em;
  }
  .hours-title__colon { color: var(--grey); }
  .hours {
    font-size: 32px;
    font-weight: 700;
    color: var(--green);
  }
  .hours--mornings { top: 492px; }
  .hours--evenings { top: 582px; }
  .hours--appointment { top: 673px; }
  .contact {
    font-size: 28px;
    font-weight: 600;
    color: var(--lime);
  }
  .contact--phone { top: 758px; left: -14px; }
  .contact--web { top: 799px; left: -14px; }
</style>
</head>
<body>
  <main class="sign">
    <svg class="sign__mark" viewBox="0 0 106 106" aria-hidden="true">
      <circle cx="53" cy="53" r="50" fill="var(--lime)"/>
    </svg>

    <h1 class="line doctor-name">Dr. med. Jonas Walbrecht</h1>
    <p class="line specialty specialty--internal">Facharzt für Innere Medizin</p>
    <p class="line specialty specialty--general">Facharzt für Allgemeinmedizin</p>

    <h2 class="line hours-title">Sprechzeiten<span class="hours-title__colon">:</span></h2>
    <p class="line hours hours--mornings">Montag bis Freitag 07:30 – 12:00 Uhr</p>
    <p class="line hours hours--evenings">Dienstag und Donnerstag 17:00 – 19:00 Uhr</p>
    <p class="line hours hours--appointment">und nach Vereinbarung</p>

    <p class="line contact contact--phone">Tel: 0761 83172</p>
    <p class="line contact contact--web">www.hausarzt-beispielau.de</p>
  </main>
</body>
</html>
```